TMAF inc Business Card Design

I have a rough draft of the TMAF inc logo that I would like to use on the business card. I also attached our logo for Brindlequay.com. I also included a sample of a business card from another mortgage company that I like. We would like a tagline on the back to say "let's get started" and below Brindlequay.com
Industry/Entity Type
Business
Contact Information for Business Card
Tallvane Mortgage and Funding, inc
Dale Fenwick
Mortgage Specialist
Direct (555)214-7093
Cell (555)608-1547
Fax (555)930-2861
dale@brindlequay.com
Westmarch Office of Land Registry 04728316
QFRB 417305

```html
<!DOCTYPE html>
<html lang="en">
<head>
<meta charset="utf-8">
<title>TMAF inc Business Card</title>
<link rel="stylesheet" href="https://fonts.googleapis.com/css2?family=Open+Sans:wght@400;600;700&family=Kalam:wght@400&display=swap">
<style>
  :root {
    --stage: #e9e7e3;
    --navy: #1c2556;
    --navy-deep: #0d1738;
    --navy-mid: #1a2a5e;
    --green: #6f9a2f;
    --paper: #ffffff;
    --faint: #eceef1;
    --white: #ffffff;
  }
  * { box-sizing: border-box; margin: 0; padding: 0; }
  html, body {
    width: 1200px;
    height: 784px;
    overflow: hidden;
    background: var(--stage);
    font-family: "Open Sans", Arial, sans-serif;
  }
  .stage {
    position: relative;
    width: 1200px;
    height: 784px;
  }
  .card {
    position: absolute;
    width: 540px;
    height: 309px;
    overflow: hidden;
    box-shadow: 0 6px 18px rgba(0,0,0,0.18);
  }

  /* Back side */
  .card-back {
    left: 40px;
    top: 237px;
    background: radial-gradient(circle at 70% 45%, var(--navy-mid) 0%, var(--navy-deep) 70%);
  }
  .card-back .texture {
    position: absolute;
    inset: 0;
    background: linear-gradient(135deg, rgba(255,255,255,0.03), rgba(0,0,0,0.12));
  }
  .tagline {
    position: absolute;
    left: 0;
    right: 0;
    top: 104px;
    text-align: center;
    font-family: "Kalam", cursive;
    font-size: 27px;
    color: var(--green);
  }
  .web-address {
    position: absolute;
    left: 0;
    right: 0;
    top: 208px;
    text-align: center;
    font-size: 19px;
    letter-spacing: 5px;
    color: var(--white);
  }

  /* Front side */
  .card-front {
    left: 620px;
    top: 237px;
    background: var(--paper);
  }
  .faint-mark {
    position: absolute;
    right: -30px;
    top: 40px;
    width: 190px;
    height: 190px;
    border-radius: 50%;
    background: var(--faint);
  }
  .person {
    position: absolute;
    right: 26px;
    top: 18px;
    text-align: left;
  }
  .person-name {
    font-size: 17px;
    font-weight: 700;
    color: var(--green);
  }
  .person-role {
    font-size: 10px;
    font-weight: 600;
    color: var(--navy);
    margin-top: 2px;
  }
  .brand {
    position: absolute;
    left: 34px;
    top: 84px;
    display: flex;
    align-items: center;
    gap: 12px;
  }
  .brand-dot {
    width: 44px;
    height: 44px;
    border-radius: 50%;
    background: var(--green);
  }
  .brand-name {
    font-size: 30px;
    font-weight: 700;
    color: var(--navy);
    line-height: 1;
  }
  .brand-line {
    position: absolute;
    left: 90px;
    top: 128px;
    font-size: 12px;
    font-weight: 600;
    color: var(--navy);
  }
  .contacts {
    position: absolute;
    left: 34px;
    top: 180px;
    list-style: none;
  }
  .contacts li {
    display: flex;
    align-items: flex-start;
    gap: 8px;
    font-size: 13.5px;
    line-height: 19px;
    color: var(--navy);
  }
  .contacts svg {
    width: 14px;
    height: 14px;
    margin-top: 3px;
    flex: none;
    fill: var(--green);
  }
</style>
</head>
<body>
<main class="stage">

  <section class="card card-back" aria-label="Card back">
    <div class="texture" role="img" aria-label="Deep navy background with fine dot texture"></div>
    <p class="tagline">let's get started</p>
    <p class="web-address">Brindlequay.com</p>
  </section>

  <section class="card card-front" aria-label="Card front">
    <div class="faint-mark" aria-hidden="true"></div>

    <div class="person">
      <p class="person-name">Dale Fenwick</p>
      <p class="person-role">Mortgage Specialist</p>
    </div>

    <div class="brand">
      <span class="brand-dot" aria-hidden="true"></span>
      <span class="brand-name">TMAF inc</span>
    </div>
    <p class="brand-line">Tallvane Mortgage and Funding.com</p>

    <ul class="contacts">
      <li>
        <svg viewBox="0 0 16 16" aria-hidden="true"><path d="M3 1h3l1.5 4-2 1.3a9 9 0 0 0 4.2 4.2L11 8.5l4 1.5v3c0 1-1 2-2 2A13 13 0 0 1 1 3c0-1 1-2 2-2z"/></svg>
        (555)214-7093
      </li>
      <li>
        <svg viewBox="0 0 16 16" aria-hidden="true"><path d="M4 0h8a1 1 0 0 1 1 1v14a1 1 0 0 1-1 1H4a1 1 0 0 1-1-1V1a1 1 0 0 1 1-1zm1 2v10h6V2zm3 11a1 1 0 1 0 0 2 1 1 0 0 0 0-2z"/></svg>
        (555)608-1547
      </li>
      <li>
        <svg viewBox="0 0 16 16" aria-hidden="true"><path d="M4 1h7v4H4zM1 6h14v8H1zm3 2v2h8V8z"/></svg>
        (555)930-2861
      </li>
      <li>
        <svg viewBox="0 0 16 16" aria-hidden="true"><path d="M1 3h14v10H1zm1.5 1.5L8 9l5.5-4.5z"/></svg>
        dale@brindlequay.com
      </li>
      <li>
        <svg viewBox="0 0 16 16" aria-hidden="true"><path d="M8 1l7 6h-2v8h-4v-5H7v5H3V7H1z"/></svg>
        <span>Westmarch Office of Land Registry<br>04728316 QFRB 417305</span>
      </li>
    </ul>
  </section>

</main>
</body>
</html>
```